Informational Business Handout needs Company Information

We have this informational handout that we would like to start handing out to clients; however, the original designer failed to include any of our company contact information. Our main request is that you redesign this card with the appropriate contact information as listed below. We would like the information/content that is currently on the card to be on the new design as well. Feel free to take liberty with the rest of the card design, or not. Please see the card specifications and our company contact information below.

Card details: 7 x 5 inches (17.78 x 12.5 cm). Cardstock.

Company Contact Details:
Dorian Maskell, JD
TrueMark, PLLC
538 E. Harlow Ave, Ste. 410, St. George, UT 84913
hello@truemark-example.com
(435) 555-0172

```html
<!DOCTYPE html>
<html lang="en">
<head>
<meta charset="utf-8">
<title>Special Needs Trust Handouts – TrueMark</title>
<link rel="stylesheet" href="https://fonts.googleapis.com/css2?family=Montserrat:wght@300;400;500;600;700;800&display=swap">
<style>
  :root {
    --stage: #5b5b5b;
    --card: #ffffff;
    --rust: #8c4a3b;
    --navy: #2a3658;
    --ink: #111111;
    --body: #2a2a2a;
    --band-start: #263a68;
    --band-mid: #4b3a5c;
    --band-end: #9b5440;
    --white: #ffffff;
  }
  * { box-sizing: border-box; margin: 0; padding: 0; }
  html, body {
    width: 1008px; height: 1200px; overflow: hidden;
    background: var(--stage);
    font-family: "Montserrat", Arial, sans-serif;
  }
  .handout {
    position: absolute; left: 168px; width: 672px; height: 480px;
    background: var(--card);
    box-shadow: 0 2px 6px rgba(0,0,0,.35);
    display: flex; flex-direction: column;
  }
  .handout--third-party { top: 71px; }
  .handout--first-party { top: 600px; }
  .handout__content { flex: 1; padding: 32px 34px 0 34px; }
  .handout--first-party .handout__content { padding: 30px 34px 0 30px; }
  .handout__title {
    font-weight: 700; font-size: 23.5px; line-height: 24px; letter-spacing: .1px;
    text-transform: uppercase;
  }
  .handout__title .accent { color: var(--rust); display: block; }
  .handout__title .main { color: var(--navy); display: block; }
  .handout__intro {
    margin-top: 13px; font-weight: 400; font-size: 14.4px; line-height: 18px; color: var(--body);
  }
  .handout--third-party .handout__intro { font-weight: 300; }
  .handout__prompt { margin-top: 17px; font-weight: 700; font-size: 15.4px; color: var(--ink); }
  .handout--first-party .handout__prompt { margin-top: 12px; }
  .checklist { list-style: none; margin-top: 18px; }
  .handout--first-party .checklist { margin-top: 12px; }
  .checklist__item {
    position: relative; padding-left: 22px; font-weight: 500; font-size: 14.6px; line-height: 17.5px;
    color: var(--ink); margin-bottom: 12.5px;
  }
  .handout--first-party .checklist__item { font-weight: 600; margin-bottom: 2.6px; }
  .checklist__item::before {
    content: ""; position: absolute; left: 0; top: 2px; width: 13px; height: 13px;
    border: 1.3px solid var(--ink); border-radius: 3px;
  }
  .handout__closing {
    margin-top: 20px; font-weight: 300; font-size: 14.4px; line-height: 18px; color: var(--body);
  }
  .handout--first-party .handout__closing { margin-top: 7px; font-weight: 400; margin-left: -2px; }
  .contact-band {
    height: 84px; display: flex; align-items: center;
    background: linear-gradient(90deg, var(--band-start), var(--band-mid) 50%, var(--band-end));
    color: var(--white); padding: 0 0 0 30px;
  }
  .brand { width: 218px; display: flex; align-items: center; gap: 10px; }
  .brand__mark { width: 12px; height: 12px; background: var(--white); }
  .brand__name { font-weight: 500; font-size: 16px; letter-spacing: 3px; }
  .contact-band__divider { width: 1px; height: 50px; background: rgba(255,255,255,.8); }
  .attorney { padding: 0 12px 0 14px; font-size: 13.4px; line-height: 17px; }
  .attorney__name { font-weight: 600; }
  .attorney__line { display: flex; align-items: center; gap: 8px; }
  .attorney__line--phone { font-weight: 700; }
  .attorney__line svg { width: 12px; height: 12px; flex: none; }
  .firm { padding-left: 11px; font-size: 13.4px; line-height: 17px; }
  .firm__name { font-weight: 600; }
</style>
</head>
<body>

<article class="handout handout--third-party">
  <div class="handout__content">
    <h1 class="handout__title">
      <span class="accent">Is a Third-Party Supplemental Needs</span>
      <span class="main">Trust Necessary for Your Estate Plan?</span>
    </h1>
    <p class="handout__intro">Will one of your intended beneficiaries, who has a physical or mental medical-ly-recognized disability, be disqualified by the Social Security Administration or other support should they receive any substantial financial gains?</p>
    <h2 class="handout__prompt">Does the intended beneficiary...</h2>
    <ul class="checklist">
      <li class="checklist__item">Currently receive or will be applying for Social Security Income?</li>
      <li class="checklist__item">Currently receive, or plan to apply for Medicaid?</li>
      <li class="checklist__item">Want to maintain or qualify for Social Security Income and/or Medicaid after benefitting from an inheritance?</li>
    </ul>
    <p class="handout__closing">If you have an intended beneficary with a recognized disability and you answered yes to any of these questions, you should contact our office to discuss whether a Third-Party Supplemental Needs Trust is right for your estate plan.</p>
  </div>
  <footer class="contact-band">
    <div class="brand"><span class="brand__mark"></span><span class="brand__name">TRUEMARK</span></div>
    <span class="contact-band__divider"></span>
    <div class="attorney">
      <div class="attorney__name">Dorian Maskell, JD</div>
      <div class="attorney__line attorney__line--phone">
        <svg viewBox="0 0 24 24"><path fill="#fff" d="M6.6 10.8a15.1 15.1 0 0 0 6.6 6.6l2.2-2.2c.3-.3.7-.4 1-.2 1.1.4 2.3.6 3.6.6.6 0 1 .4 1 1V20c0 .6-.4 1-1 1A17 17 0 0 1 3 4c0-.6.4-1 1-1h3.5c.6 0 1 .4 1 1 0 1.3.2 2.5.6 3.6.1.3 0 .7-.2 1z"/></svg>
        (435) 555-0172</div>
      <div class="attorney__line">
        <svg viewBox="0 0 24 24"><path fill="#fff" d="M2 5h20v14H2z"/><path fill="none" stroke="#4b3a5c" stroke-width="2" d="M2 5l10 8 10-8"/></svg>
        hello@truemark-example.com</div>
    </div>
    <span class="contact-band__divider"></span>
    <div class="firm">
      <div class="firm__name">TrueMark, PLLC,</div>
      <div>538 E. Harlow Ave,</div>
      <div>Ste. 410, St. George, UT 84913</div>
    </div>
  </footer>
</article>

<article class="handout handout--first-party">
  <div class="handout__content">
    <h1 class="handout__title">
      <span class="accent">Is a First-Party Special Needs Trust</span>
      <span class="main">Right for You?</span>
    </h1>
    <p class="handout__intro">Do you have a disability recognized&nbsp; by the Social Security Administration which can be expected to result in death or which has lasted or can be expected to last for a continuous period of not less than twelve months?</p>
    <h2 class="handout__prompt">Are you...</h2>
    <ul class="checklist">
      <li class="checklist__item">Are you under age 65 and...?</li>
      <li class="checklist__item">Expecting&nbsp; settlement proceeds from the negligent actions of a third party?</li>
      <li class="checklist__item">Expecting an inheritance?</li>
      <li class="checklist__item">Currently recieving, or will be applying for Social Security Income?</li>
      <li class="checklist__item">Currently receiving, or will be applying for Medicaid?</li>
      <li class="checklist__item">Wanting to maintain or qualify for Social Security Income and/or Medicaid after being awarded your settlement or inheritance?</li>
    </ul>
    <p class="handout__closing">If you have a recognized disability and you answered yes to any of these questions, you should contact our office to discuss whether a Fist-Party Special Needs trust is right for you.</p>
  </div>
  <footer class="contact-band">
    <div class="brand"><span class="brand__mark"></span><span class="brand__name">TRUEMARK</span></div>
    <span class="contact-band__divider"></span>
    <div class="attorney">
      <div class="attorney__name">Dorian Maskell, JD</div>
      <div class="attorney__line attorney__line--phone">
        <svg viewBox="0 0 24 24"><path fill="#fff" d="M6.6 10.8a15.1 15.1 0 0 0 6.6 6.6l2.2-2.2c.3-.3.7-.4 1-.2 1.1.4 2.3.6 3.6.6.6 0 1 .4 1 1V20c0 .6-.4 1-1 1A17 17 0 0 1 3 4c0-.6.4-1 1-1h3.5c.6 0 1 .4 1 1 0 1.3.2 2.5.6 3.6.1.3 0 .7-.2 1z"/></svg>
        (435) 555-0172</div>
      <div class="attorney__line">
        <svg viewBox="0 0 24 24"><path fill="#fff" d="M2 5h20v14H2z"/><path fill="none" stroke="#4b3a5c" stroke-width="2" d="M2 5l10 8 10-8"/></svg>
        hello@truemark-example.com</div>
    </div>
    <span class="contact-band__divider"></span>
    <div class="firm">
      <div class="firm__name">TrueMark, PLLC,</div>
      <div>538 E. Harlow Ave,</div>
      <div>Ste. 410, St. George, UT 84913</div>
    </div>
  </footer>
</article>

</body>
</html>
```